SEO optimized website for Nu-Crest Corporate identity

I need an eye catching website (Flash splash is OK-I think) to help me promote my company of 10 years: Nu-Crest Inc. - we recently just awarded a design win for my logo design. See attached files.

The company name is Nu-Crest Inc. My current website is www.nu-crest.ca and we specialize in large infrastructure - technology integration, both management and engineering. We have worked almost exclusively on KORB projects and wish to promote that.

I need it to be flexible enough for me to add pages for existing case studies and future case studies.

It is difficult to marry technology and green but do your best as I would like to highlight our KORB AP staff members.

The other side of my business is Small Medium Sized Business support and engineering. VOIP, Server, Desktop we have done it all.

My current site is www.nu-crest.ca
Updates

Please use newly attached logo for designs.

All Please see some sample images to incorporate into the deisgns

Reason: Need more time to evaluate

Please use the correct/new logo in all designs

Please use the updated l;og that was included. Thank you.

Reason: I would like designers to modify their deisgns with the actual company logo. Only one design er has gotten it right. Please modify.

Reason: Still no time to devote to this. Sorry

Reason: Not ready to focus on it

Please only use the logo supplied int he source file zip

Target Market(s)

Both large infrstructure facility owners and small and medium sized businesses.

Industry/Entity Type

Business

Requirements
Must have
• SEO optimization
Easy for me to provide content going forward
Link to my FTP site
Links to my main partners
Separate login are for my clients to store files

```html
<!DOCTYPE html>
<html lang="en">
<head>
<meta charset="utf-8">
<title>Nu-Crest Inc. | Home</title>
<meta name="description" content="Nu-Crest Inc. – large infrastructure technology integration, management and engineering, plus SMB support.">
<link rel="stylesheet" href="https://fonts.googleapis.com/css2?family=Michroma&family=Roboto:wght@300;400;500&display=swap">
<style>
  :root {
    --orange: #f26b0a;
    --teal: #3aa99b;
    --charcoal: #2f2f2f;
    --button: #5b5b5b;
    --navy: #13324f;
    --text: #222;
    --text-light: #666;
    --page-bg: #e3e5df;
    --header-bg: #eef0eb;
    --footer-bg: #e9ebe6;
    --link-blue: #3a6aa8;
    --white: #fff;
  }
  * { box-sizing: border-box; margin: 0; padding: 0; }
  html, body { width: 1094px; height: 1200px; overflow: hidden; }
  body {
    position: relative;
    background: var(--page-bg);
    font-family: "Roboto", Arial, sans-serif;
    color: var(--text);
  }
  .display { font-family: "Michroma", "Arial Black", sans-serif; font-variant: small-caps; }

  /* Header */
  .site-header { position: absolute; left: 0; top: 0; width: 1094px; height: 150px; background: var(--header-bg); border-top: 5px solid #666; }
  .brand { position: absolute; left: 128px; top: 17px; display: flex; align-items: center; gap: 10px; text-decoration: none; }
  .brand-mark { width: 66px; height: 66px; background: var(--navy); }
  .brand-name { font-family: "Roboto", sans-serif; font-weight: 300; font-size: 46px; color: var(--navy); letter-spacing: -1px; }
  .main-nav a {
    position: absolute; top: 104px; font-size: 13px; font-weight: 700; letter-spacing: 1.5px;
    color: var(--navy); text-decoration: none;
  }
  .main-nav a.active { color: var(--orange); padding-bottom: 8px; border-bottom: 3px solid var(--orange); }

  /* Panels */
  .panel { position: absolute; background: var(--white); }
  .tab {
    position: absolute; height: 48px; color: var(--white); font-size: 21px; letter-spacing: 3px;
    display: flex; align-items: center; padding-left: 12px; white-space: nowrap;
  }
  .tab::after {
    content: ""; position: absolute; bottom: -9px; border-top: 9px solid var(--tab-color); border-right: 10px solid transparent;
    left: var(--pointer, 120px);
  }
  .tab-orange { background: var(--orange); --tab-color: var(--orange); }
  .tab-teal { background: var(--teal); --tab-color: var(--teal); }
  .tab-dark { background: var(--charcoal); --tab-color: var(--charcoal); }

  .hero-intro { position: absolute; left: 144px; top: 232px; width: 212px; font-size: 12.5px; font-weight: 300; line-height: 19.4px; color: var(--text-light); }
  .hero-photo { position: absolute; left: 379px; top: 187px; width: 564px; height: 227px; background: linear-gradient(100deg, #b7b4b0 0%, #d9d2cb 35%, #8f96a0 65%, #3a3d46 100%); }
  .hero-caption {
    position: absolute; left: 538px; top: 358px; width: 405px; height: 48px; background: rgba(190, 40, 50, 0.72);
    color: var(--white); font-size: 16.5px; font-weight: 300; display: flex; align-items: center; padding-left: 7px; white-space: nowrap;
  }

  .about-text { position: absolute; left: 137px; top: 516px; width: 370px; font-size: 12.3px; line-height: 14.6px; }
  .about-text p + p { margin-top: 14.6px; }
  .section-title { position: absolute; left: 138px; font-size: 15px; letter-spacing: 2.5px; color: var(--navy); font-weight: 700; }
  .capabilities { position: absolute; left: 136px; top: 742px; list-style: none; }
  .capabilities li { height: 24.6px; display: flex; align-items: center; font-size: 12.5px; font-weight: 500; }
  .cap-icon { width: 14px; height: 14px; border-radius: 50%; margin-right: 16px; }
  .quick-links { position: absolute; left: 142px; top: 940px; list-style: none; }
  .quick-links li { height: 26.4px; display: flex; align-items: center; font-size: 13px; font-weight: 300; }
  .quick-links li::before { content: ""; width: 6px; height: 6px; border: 1px solid #bbb; border-radius: 50%; margin-right: 17px; }
  .quick-links a { color: var(--navy); }

  .testimonial-text { position: absolute; left: 570px; top: 509px; width: 352px; font-size: 13px; font-weight: 300; line-height: 17.6px; color: #444; }
  .testimonial-author { position: absolute; left: 572px; top: 605px; font-size: 13px; font-weight: 300; color: #444; }
  .read-more { position: absolute; left: 765px; top: 630px; text-decoration: none; }

  .partner-name { position: absolute; font-family: "Roboto", sans-serif; font-weight: 500; color: #333; white-space: nowrap; }

  /* Footer */
  .site-footer { position: absolute; left: 0; top: 1091px; width: 1094px; height: 109px; background: var(--footer-bg); }
  .footer-nav a { position: absolute; top: 13px; font-size: 11.5px; font-weight: 700; letter-spacing: 1.5px; color: #666; text-decoration: none; }
  .footer-brand { position: absolute; left: 127px; top: 34px; display: flex; align-items: center; gap: 10px; opacity: 0.35; }
  .footer-brand .brand-mark { width: 64px; height: 64px; background: #777; }
  .footer-brand .brand-name { color: #777; }
  .copyright { position: absolute; right: 145px; top: 76px; font-size: 12.5px; font-weight: 300; color: var(--link-blue); }
</style>
</head>
<body>

<header class="site-header">
  <a class="brand" href="#">
    <span class="brand-mark"></span>
    <span class="brand-name">Nu-Crest</span>
  </a>
  <nav class="main-nav display">
    <a class="active" href="#" style="left:321px">Home</a>
    <a href="#" style="left:402px">About Us</a>
    <a href="#" style="left:523px">Services</a>
    <a href="#" style="left:636px">Partners</a>
    <a href="#" style="left:754px">Creers</a>
    <a href="#" style="left:853px">Contacts</a>
  </nav>
</header>

<main>
  <!-- Hero -->
  <section class="panel" style="left:127px;top:187px;width:816px;height:227px"></section>
  <h1 class="tab tab-orange display" style="left:115px;top:170px;width:173px;padding-left:39px;font-size:24px;--pointer:116px">Home</h1>
  <p class="hero-intro">It is a long established fact that a reader will be distracted by the read-able content of a page when looking at its layout. The point of using Lorem Ipsum is that it has a more-or-less normal distribution of lettersThe point of using Lorem Ipsum is that it has a more-or-less normal distribution of letters</p>
  <div class="hero-photo" role="img" aria-label="Team of five smiling business professionals in suits"></div>
  <div class="hero-caption">NU-CREST ACHIEVE THE PROMISE OF TECHNOLOGY</div>

  <!-- About -->
  <section class="panel" style="left:127px;top:460px;width:396px;height:618px"></section>
  <h2 class="tab tab-orange display" style="left:115px;top:444px;width:385px;--pointer:116px">Nu-Crest Technology</h2>
  <div class="about-text">
    <p>It is a long established fact that a reader will be distracted by the readable content of a page when looking at its layout. The point of using Lorem Ipsum is that it has a more-or-less normal distribution of letters, as opposed to using 'Content here, content here', making it look like readable English. Many desktop publishing packages and web page editors .</p>
    <p>now use Lorem Ipsum as their default model text, and a search for 'lorem ipsum' will uncover many web sites still in their infancy. Various versions have evolved over the years, sometimes by acci-dent, sometimes on purpose (injected humour and the like).</p>
  </div>

  <h3 class="section-title display" style="top:705px">Core Capabilities</h3>
  <ul class="capabilities">
    <li><span class="cap-icon" style="background:#9bbf7a"></span>-Project Management</li>
    <li><span class="cap-icon" style="background:#a5a5a5"></span>-IBT</li>
    <li><span class="cap-icon" style="background:#4d77b5"></span>-SMB Support</li>
    <li><span class="cap-icon" style="background:#a8b6e0"></span>-Virtualization</li>
    <li><span class="cap-icon" style="background:#3c5e86"></span>-Voice Technologies</li>
    <li><span class="cap-icon" style="background:#2f8fd8"></span>-Technology Construction</li>
  </ul>

  <h3 class="section-title display" style="top:911px">Core Capabilities</h3>
  <ul class="quick-links">
    <li><a href="#">Nu-Crest FTP</a></li>
    <li><a href="#">Web Timesheet</a></li>
    <li><a href="#">Nu-Crest for Clients</a></li>
    <li><a href="#">Job Sites Photos</a></li>
    <li><a href="#">Free FTP Client Software</a></li>
  </ul>

  <!-- Testimonial -->
  <section class="panel" style="left:546px;top:460px;width:397px;height:231px"></section>
  <h2 class="tab tab-teal display" style="left:566px;top:443px;width:194px;padding-left:7px;--pointer:117px">Testimonial</h2>
  <p class="testimonial-text">The Meridian Group of Companies was formed in 2005 to provide dealers and manufacturers of office furniture and their clients with a suite of services supplying cost efficient, world-class solutions in the areas of distribution, delivery, service, warehousing, installation,</p>
  <p class="testimonial-author">Mr.Alan Brooks,Westmere Company</p>
  <a class="read-more" href="#">
    <svg width="130" height="26" viewBox="0 0 130 26">
      <polygon points="0,0 120,0 130,13 120,26 0,26" fill="#5b5b5b"/>
      <text x="15" y="17" fill="#fff" font-family="Michroma, sans-serif" font-size="9.5" font-weight="700" letter-spacing="1.5">READ MORE</text>
    </svg>
  </a>

  <!-- Partners -->
  <section class="panel" style="left:546px;top:728px;width:399px;height:350px"></section>
  <h2 class="tab tab-dark display" style="left:567px;top:709px;width:263px;padding-left:7px;--pointer:168px">Partners Logos</h2>
  <span class="partner-name" style="left:570px;top:790px;font-size:30px">Vantrel</span>
  <span class="partner-name" style="left:778px;top:818px;font-size:26px">Orlexa</span>
  <span class="partner-name" style="left:578px;top:896px;font-size:42px">Quadrix</span>
  <span class="partner-name" style="left:778px;top:912px;font-size:24px">Vantrel</span>
  <span class="partner-name" style="left:622px;top:988px;font-size:30px">Brightline AV</span>
</main>

<footer class="site-footer">
  <nav class="footer-nav display">
    <a href="#" style="left:127px">Home</a>
    <a href="#" style="left:208px">About Us</a>
    <a href="#" style="left:328px">Services</a>
    <a href="#" style="left:442px">Partners</a>
    <a href="#" style="left:560px">Creers</a>
    <a href="#" style="left:658px">Contacts</a>
  </nav>
  <div class="footer-brand">
    <span class="brand-mark"></span>
    <span class="brand-name">Nu-Crest</span>
  </div>
  <p class="copyright">Copyright © 2010, Nu-Crest. All rights reserved.</p>
</footer>

</body>
</html>
```